Mosquito Mosquito & garden protection

The uploaded logo must be integrated as the main theme of the card. I would like it to be modern and eye catching. Maybe some backround images or light silver metallic background.
Space enough at the base for contact info to be put in- phone numbers,emails,names,website.
Space on the back for short blog and lines for hand writing..calling card.
Commercial- golf courses, schools, outdoor function properties, pre event treatments.
Residential- retirement villages, townhome complexes and general houses
Management

```html
<!DOCTYPE html>
<html lang="en">
<head>
<meta charset="utf-8">
<title>Tidewater Yard Care – Business Card</title>
<link rel="stylesheet" href="https://fonts.googleapis.com/css2?family=Crimson+Text:wght@400;600;700&display=swap">
<style>
  :root {
    --stage: #e6e6e6;
    --paper: #ffffff;
    --ink: #231f20;
    --brand-red: #e11f2d;
    --on-dark: #ffffff;
    --serif: "Crimson Text", Georgia, serif;
  }
  * { box-sizing: border-box; margin: 0; padding: 0; }
  html, body {
    width: 1200px; height: 900px; overflow: hidden;
    background: var(--stage);
    font-family: var(--serif);
  }
  .canvas { position: relative; width: 1200px; height: 900px; }

  .card {
    position: absolute; width: 700px; height: 400px;
    background: var(--paper);
    box-shadow: 0 10px 24px rgba(0,0,0,.18);
    overflow: hidden;
  }
  .card--front { left: 80px; top: 50px; }
  .card--back  { left: 420px; top: 480px; }

  .card__bands { position: absolute; inset: 0; }

  .brand { position: absolute; left: 36px; top: 58px; }
  .brand__name {
    display: flex; align-items: center; gap: 12px;
    font-size: 40px; font-weight: 400; letter-spacing: 0;
    color: var(--ink); line-height: 1;
  }
  .brand__square { width: 14px; height: 14px; background: var(--brand-red); }
  .brand__tagline {
    margin-top: 10px;
    font-size: 18px; font-weight: 400; letter-spacing: .5px;
    color: var(--ink);
  }

  .contact {
    position: absolute; left: 484px; top: 176px;
    list-style: none; color: var(--on-dark); font-size: 16px; line-height: 1.45;
  }
  .contact li { display: flex; align-items: center; gap: 10px; }
  .contact svg { width: 11px; height: 11px; fill: var(--brand-red); flex: none; }

  .person { position: absolute; left: 32px; top: 300px; color: var(--on-dark); }
  .person__name { font-size: 27px; font-weight: 700; letter-spacing: .5px; text-transform: uppercase; line-height: 1.1; }
  .person__role { font-size: 15px; letter-spacing: 1px; text-transform: uppercase; }

  .back__rule { position: absolute; left: 60px; top: 300px; width: 560px; height: 2px; background: var(--brand-red); transform: rotate(-3deg); transform-origin: left center; }
  .back__web {
    position: absolute; right: 40px; top: 320px;
    font-size: 24px; font-weight: 600; letter-spacing: 1px; color: var(--ink);
  }
</style>
</head>
<body>
<main class="canvas">

  <section class="card card--front" aria-label="Card front">
    <svg class="card__bands" viewBox="0 0 700 400" aria-hidden="true">
      <polygon points="445,150 700,150 700,400 352,400" fill="var(--ink)"/>
      <polygon points="0,265 390,265 340,400 0,400" fill="var(--brand-red)"/>
    </svg>

    <div class="brand">
      <p class="brand__name"><span class="brand__square"></span><span>Tidewater Yard Care</span></p>
      <p class="brand__tagline">Mosquito &amp; garden protection</p>
    </div>

    <ul class="contact">
      <li><svg viewBox="0 0 12 12"><path d="M2.5 1l2 2-1 1.3c.6 1.4 1.8 2.6 3.2 3.2L8 6.5l2 2-1.2 1.8C5 10 2 7 1.7 2.2z"/></svg>+330-5550-0142</li>
      <li><svg viewBox="0 0 12 12"><path d="M1 2.5h10v7H1zM1.8 3.3L6 6.6l4.2-3.3v.9L6 7.5 1.8 4.2z"/></svg>hello@tidewateryard.com</li>
      <li><svg viewBox="0 0 12 12"><circle cx="6" cy="6" r="5"/></svg>www.tidewateryard.com</li>
    </ul>

    <div class="person">
      <p class="person__name">Dana Whitfield</p>
      <p class="person__role">Director</p>
    </div>
  </section>

  <section class="card card--back" aria-label="Card back">
    <div class="back__rule"></div>
    <p class="back__web">www.tidewateryard.com</p>
  </section>

</main>
</body>
</html>
```